Brightpath Holdings Business Card

Create a two sided, high gloss, quality business card for Brightpath Holdings.

Target Market(s)

People wanting to purchase, scale, and sell businesses.

Industry/Entity Type

Entrepreneurs

Contact Information for Business Card

One line: Dana Corwell, CPA, CMA Another line: Entrepreneur & Investor Another line: Business Ownership Transition Expert Another line: Multi-State Licensed Real Estate Broker Phone 954-BRTPATH (278-7284) Email Dana@Brightpath Holdings.com Website www.Brightpath.com

Requirements
Must have
• Black Card, logo on one side, all other information on the other side including a small logo.
Nice to have
• Possibly add a tagline "Helping entrepreneurs live a life they don't need a vacation from"
Should not have
• There will not be a mailing address on these cards.

```html
<!DOCTYPE html>
<html lang="en">
<head>
<meta charset="utf-8">
<title>Brightpath Holdings Business Card</title>
<link rel="stylesheet" href="https://fonts.googleapis.com/css2?family=Tinos:wght@400;700&display=swap">
<style>
  :root {
    --backdrop: #d9d8d8;
    --card-black: #141414;
    --card-black-soft: #1f1f1f;
    --gold: #d9b24a;
    --gold-light: #f6e7a8;
    --gold-deep: #b88a2a;
    --ink-dark: #111111;
    --ink-light: #f1f1f1;
  }
  * { box-sizing: border-box; margin: 0; padding: 0; }
  html, body {
    width: 1200px; height: 799px; overflow: hidden;
    background: var(--backdrop);
    font-family: "Tinos", "Times New Roman", serif;
  }
  .canvas {
    position: relative; width: 1200px; height: 799px;
  }
  .card {
    position: absolute; top: 245px;
    width: 540px; height: 310px;
    background: radial-gradient(ellipse at 40% 20%, var(--card-black-soft), var(--card-black) 70%);
    overflow: hidden;
  }
  .card--front { left: 40px; }
  .card--back { left: 620px; }

  /* Front */
  .front-brand {
    position: absolute; left: 0; right: 0; top: 110px;
    display: flex; justify-content: center; align-items: center; gap: 14px;
  }
  .brand-dot {
    width: 30px; height: 30px; border-radius: 50%;
    background: var(--gold);
  }
  .brand-name {
    font-size: 40px; font-weight: 700; color: var(--gold);
    letter-spacing: 0.5px;
  }
  .tagline-band {
    position: absolute; left: 0; right: 0; top: 232px; height: 26px;
    background: linear-gradient(90deg, var(--gold-light), #fff6cf 45%, var(--gold-light));
    display: flex; align-items: center; justify-content: center;
  }
  .tagline {
    font-size: 16px; color: var(--ink-dark);
  }

  /* Back */
  .back-brand {
    position: absolute; left: 38px; top: 58px;
    display: flex; align-items: center; gap: 8px;
  }
  .back-brand .brand-dot { width: 16px; height: 16px; }
  .back-brand .brand-name { font-size: 19px; }

  .name-band {
    position: absolute; left: 268px; right: 0; top: 92px; height: 34px;
    border-radius: 8px 0 0 8px;
    background: linear-gradient(90deg, #f7e59a, #fff3c4 35%, var(--gold) 100%);
    display: flex; align-items: center; padding-left: 12px;
  }
  .person-name { font-size: 22px; color: var(--ink-dark); }
  .titles {
    position: absolute; left: 262px; top: 134px;
    color: var(--ink-light); font-size: 15.5px; line-height: 19px;
    list-style: none;
  }
  .contact-rail {
    position: absolute; left: 0; top: 0; width: 540px; height: 310px;
  }
  .contact {
    position: absolute; top: 250px;
    color: var(--ink-light); font-size: 14px; white-space: nowrap;
    transform: translateX(-50%);
  }
</style>
</head>
<body>
<main class="canvas">

  <section class="card card--front" aria-label="Card front">
    <div class="front-brand">
      <span class="brand-dot"></span>
      <span class="brand-name">Brightpath Holdings</span>
    </div>
    <div class="tagline-band">
      <p class="tagline">Helping entrepreneurs live a life they don't need a vacation from</p>
    </div>
  </section>

  <section class="card card--back" aria-label="Card back">
    <div class="back-brand">
      <span class="brand-dot"></span>
      <span class="brand-name">Brightpath Holdings</span>
    </div>

    <div class="name-band"><h1 class="person-name">Dana Corwell, CPA, CMA</h1></div>
    <ul class="titles">
      <li>Entrepreneur &amp; Investor</li>
      <li>Business Ownership Transition Expert</li>
      <li>Multi-State Licensed Real Estate Broker</li>
    </ul>

    <svg class="contact-rail" viewBox="0 0 540 310" aria-hidden="true">
      <defs>
        <linearGradient id="goldFill" x1="0" y1="0" x2="1" y2="1">
          <stop offset="0" stop-color="#f6e7a8"/>
          <stop offset="0.5" stop-color="#d9b24a"/>
          <stop offset="1" stop-color="#a8791f"/>
        </linearGradient>
      </defs>
      <line x1="0" y1="212" x2="540" y2="212" stroke="url(#goldFill)" stroke-width="2.5"/>
      <!-- phone -->
      <g transform="translate(95 212)">
        <circle r="17" fill="url(#goldFill)" stroke="#f6e7a8" stroke-width="1"/>
        <path d="M-6 -8 l4 0 l2 5 l-2.5 2 q2 4 6 6 l2 -2.5 l5 2 l0 4 q-1 2 -4 2 q-9 -1 -14 -10 q-2 -4 -1 -7 q1 -1.5 2.5 -1.5z" fill="#1a1a1a"/>
      </g>
      <!-- envelope -->
      <g transform="translate(275 212)">
        <circle r="17" fill="url(#goldFill)" stroke="#f6e7a8" stroke-width="1"/>
        <rect x="-9" y="-6" width="18" height="12" fill="#1a1a1a"/>
        <path d="M-9 -6 L0 2 L9 -6" fill="none" stroke="#d9b24a" stroke-width="1.4"/>
      </g>
      <!-- globe -->
      <g transform="translate(450 212)">
        <circle r="17" fill="url(#goldFill)" stroke="#f6e7a8" stroke-width="1"/>
        <g fill="none" stroke="#1a1a1a" stroke-width="1.6">
          <circle r="9"/>
          <ellipse rx="4" ry="9"/>
          <line x1="-9" y1="0" x2="9" y2="0"/>
          <line x1="-8" y1="-4.5" x2="8" y2="-4.5"/>
          <line x1="-8" y1="4.5" x2="8" y2="4.5"/>
        </g>
      </g>
    </svg>

    <p class="contact" style="left:95px">954-BRTPATH (278-7284)</p>
    <p class="contact" style="left:275px">Dana@BrightpathHoldings.com</p>
    <p class="contact" style="left:450px">www.Brightpath.com</p>
  </section>

</main>
</body>
</html>
```